Business Card for a recruitment agency specializing in engineers and geeks.

I am looking to create Business Card Design for my company.
That
## Company name:
Quorvant Inc.
Quorvant is a term coined from the following concepts.
1. geek + engineer
2. geek utopia
## Company Description:
The concept of the company is to be a recruitment agency that creates a paradise for geeky engineers. We want to be a place where engineers can have more freedom and ideal career support.
# Target.
The noun itself is often given to companies that want to hire engineers, geeks, and IT-related personnel, so it would be nice to get the impression that this company seems to have good engineers and IT personnel. There are many occasions where I meet with the human resources department, president, or senior management and give it to them.
# Atmosphere
We are happy with simplicity, but with an impact that will help people remember the company. The logo is based on a dinosaur that does programming, so it should be somewhat playful, but since it will basically be used in a business setting, please don't make it too silly.
# About the logo
See the attached files. The company logo represents our engineers smiling upward because of our work, with the motif of a dinosaur doing programming.
## Color
We will leave the color scheme to you, but since the logo is in black and white, colors with such a taste would fit well.
## file format
ai, psd, png, svg
Industry/Entity Type
human resource and employment agency
Contact Information for Business Card
Company name, address, email, tel, URL,logo
Colors
Designer to choose colors to be used in the design.

```html
<!DOCTYPE html>
<html lang="en">
<head>
<meta charset="utf-8">
<title>Quorvant Inc. Business Card</title>
<link rel="stylesheet" href="https://fonts.googleapis.com/css2?family=Open+Sans:wght@400;600;700&display=swap">
<style>
  :root {
    --page-bg: #f3f4f1;
    --card-bg: #e2e7df;
    --ink: #141414;
    --muted: #f7f8f5;
    --soft: #8d9489;
    --band: #0b0b0b;
    --band-text: #ffffff;
  }
  * { margin: 0; padding: 0; box-sizing: border-box; }
  html, body {
    width: 1200px; height: 800px; overflow: hidden;
    background: var(--page-bg);
    font-family: "Open Sans", Arial, sans-serif;
  }
  .card {
    position: absolute; left: 160px; top: 150px;
    width: 880px; height: 500px;
    background: var(--card-bg);
    border-radius: 30px;
    overflow: hidden;
    box-shadow: 0 10px 30px rgba(0,0,0,0.08);
  }
  .holder { position: absolute; left: 40px; top: 100px; }
  .holder-name { font-size: 27px; font-weight: 700; color: var(--ink); letter-spacing: 0.5px; text-transform: uppercase; }
  .holder-role { font-size: 19px; color: var(--soft); margin-top: 2px; }

  .brand { position: absolute; left: 430px; top: 48px; display: flex; align-items: center; gap: 16px; }
  .brand-square { width: 40px; height: 40px; background: var(--ink); }
  .brand-name { font-size: 54px; font-weight: 600; color: var(--ink); line-height: 1; }

  .contacts { position: absolute; left: 40px; top: 296px; list-style: none; }
  .contacts li { display: flex; align-items: center; gap: 12px; height: 35px; font-size: 19px; color: var(--soft); }
  .contacts svg { width: 17px; height: 17px; fill: var(--ink); flex: none; }

  .address-band {
    position: absolute; left: 0; top: 418px; width: 720px; height: 82px;
    background: var(--band); color: var(--band-text);
    display: flex; align-items: center; gap: 14px; padding-left: 40px;
    font-size: 20px;
  }
  .address-band svg { width: 18px; height: 22px; fill: var(--band-text); flex: none; }
  .band-end {
    position: absolute; left: 810px; top: 418px; width: 70px; height: 82px;
    background: var(--band);
  }
</style>
</head>
<body>
  <section class="card" aria-label="Quorvant Inc. business card">
    <div class="holder">
      <p class="holder-name">Daniel Reeve</p>
      <p class="holder-role">President</p>
    </div>

    <div class="brand">
      <span class="brand-square" aria-hidden="true"></span>
      <span class="brand-name">Quorvant</span>
    </div>

    <ul class="contacts">
      <li>
        <svg viewBox="0 0 24 24" aria-hidden="true"><path d="M6.6 10.8a15.1 15.1 0 0 0 6.6 6.6l2.2-2.2c.3-.3.7-.4 1-.2 1.1.4 2.3.6 3.6.6.6 0 1 .4 1 1V20c0 .6-.4 1-1 1C10.6 21 3 13.4 3 4c0-.6.4-1 1-1h3.5c.6 0 1 .4 1 1 0 1.3.2 2.5.6 3.6.1.3 0 .7-.2 1z"/></svg>
        (00) 0000 0000
      </li>
      <li>
        <svg viewBox="0 0 24 24" aria-hidden="true"><path d="M3 5h18v14H3z M3 5l9 7 9-7" /><path d="M4 6.5l8 6.2 8-6.2V18H4z" fill="var(--card-bg)"/></svg>
        john@quorvantinc.com
      </li>
      <li>
        <svg viewBox="0 0 24 24" aria-hidden="true"><circle cx="12" cy="12" r="10"/><path d="M7 8c2 0 3 1 3 2s-2 1-2 3 2 2 2 4l-3 1c-2-2-3-4-3-6 0-2 1-3 3-4zM14 5c2 1 4 3 4 6-1 0-2-1-3 0s0 3-1 4l-2-2c0-2 2-2 1-4s-1-3 1-4z" fill="var(--card-bg)"/></svg>
        www.quorvantinc.com
      </li>
    </ul>

    <div class="address-band">
      <svg viewBox="0 0 18 22" aria-hidden="true"><path d="M9 0a8 8 0 0 0-8 8c0 6 8 14 8 14s8-8 8-14a8 8 0 0 0-8-8zm0 11a3 3 0 1 1 0-6 3 3 0 0 1 0 6z"/></svg>
      11 dummy city, dummy place, P.O Box 0000 Dummy Land
    </div>
    <div class="band-end" aria-hidden="true"></div>
  </section>
</body>
</html>
```